Law practice business card

I have an existing logo that I would like to make a little cleaner and maybe something more creative, but using the same base. I would like a contempoary design of the business card.

Industry/Entity Type

Law

Logo Text

On one side of the card - below the logo - I would want to say "BRANTOVE" and below that it should read "LAW OFFICES, PC" in smaller print. If you have somethign more creative, I would love to see it.

Logo styles of interest
Lettermark Logo
Font styles to use
Sans Serif

Colors

Designer to choose only greyscale colors for use in the design.

Requirements
Must have
• Standard info: My name with "Attorney at Law" underneath; phone, fax, address, email and website.

```html
<!DOCTYPE html>
<html lang="en">
<head>
<meta charset="UTF-8">
<title>Brantove Law Offices – Business Card</title>
<link rel="stylesheet" href="https://fonts.googleapis.com/css2?family=Montserrat:wght@400;500;600;700&display=swap">
<style>
  :root {
    --page-bg: #2a2b2e;
    --card-dark: #1c1c1e;
    --card-light: #ffffff;
    --brand: #3b1519;
    --ink: #2b2b2b;
    --ink-soft: #4a4a4a;
    --white: #ffffff;
    --rule-light: #bdbdbd;
  }
  * { box-sizing: border-box; margin: 0; padding: 0; }
  html, body { width: 1200px; height: 900px; overflow: hidden; }
  body {
    background: var(--page-bg);
    font-family: "Montserrat", Arial, sans-serif;
    display: flex;
    flex-direction: column;
    align-items: center;
    justify-content: center;
    gap: 46px;
  }
  .card {
    width: 672px;
    height: 384px;
    border-radius: 22px;
    position: relative;
    overflow: hidden;
  }

  /* Front (dark) */
  .card--front { background: var(--card-dark); }
  .card--front .wordmark {
    position: absolute;
    right: 60px;
    top: 150px;
    text-align: center;
    color: var(--white);
  }
  .wordmark__name-row { display: flex; align-items: center; gap: 14px; justify-content: center; }
  .wordmark__square { width: 22px; height: 22px; background: currentColor; }
  .wordmark__name {
    font-weight: 600;
    font-size: 46px;
    letter-spacing: 1px;
    line-height: 1;
  }
  .wordmark__sub {
    display: flex;
    align-items: center;
    gap: 8px;
    margin-top: 6px;
    font-size: 14px;
    font-weight: 400;
    letter-spacing: 1.5px;
  }
  .wordmark__sub::before, .wordmark__sub::after {
    content: "";
    flex: 1;
    height: 1px;
    background: currentColor;
  }

  /* Back (light) */
  .card--back {
    background: var(--card-light);
    display: flex;
    align-items: center;
  }
  .card--back .brand-panel {
    width: 360px;
    display: flex;
    justify-content: center;
    color: var(--brand);
  }
  .card--back .wordmark__name { font-size: 44px; }
  .card--back .wordmark__sub { color: var(--ink); font-size: 13px; }
  .divider {
    width: 1px;
    height: 200px;
    background: var(--brand);
  }
  .contact {
    padding-left: 34px;
    color: var(--ink);
  }
  .contact__name {
    font-weight: 700;
    font-size: 20px;
    color: var(--brand);
  }
  .contact__title {
    font-size: 13px;
    color: var(--ink-soft);
    margin-bottom: 16px;
  }
  .contact__address {
    font-size: 13px;
    line-height: 1.35;
    margin-bottom: 16px;
  }
  .contact__list { list-style: none; font-size: 13px; line-height: 1.6; }
  .contact__list li { display: flex; align-items: center; gap: 10px; }
  .contact__list svg { width: 12px; height: 12px; fill: var(--brand); flex: none; }
</style>
</head>
<body>

  <section class="card card--front" aria-label="Card front">
    <div class="wordmark">
      <div class="wordmark__name-row">
        <span class="wordmark__name">BRANTOVE</span>
      </div>
      <div class="wordmark__sub">LAW OFFICES, PC</div>
    </div>
  </section>

  <section class="card card--back" aria-label="Card back">
    <div class="brand-panel">
      <div class="wordmark">
        <div class="wordmark__name-row">
          <span class="wordmark__square"></span>
          <span class="wordmark__name">BRANTOVE</span>
        </div>
        <div class="wordmark__sub">LAW OFFICES, PC</div>
      </div>
    </div>
    <div class="divider"></div>
    <div class="contact">
      <p class="contact__name">Daniel Rourke</p>
      <p class="contact__title">Attorney at Law</p>
      <p class="contact__address">418 Harlow Avenue, #112<br>Millbrook, OH 44120</p>
      <ul class="contact__list">
        <li>
          <svg viewBox="0 0 12 12" aria-hidden="true"><path d="M2.5 0.8 4.3 3 3.4 4.4c.7 1.6 2 2.9 3.6 3.6l1.4-.9 2.2 1.8-1 2C5.2 10.7 1.3 6.8.5 2z"/></svg>
          877-555-0192
        </li>
        <li>
          <svg viewBox="0 0 12 12" aria-hidden="true"><rect x="3" y="0.5" width="6" height="3.5"/><rect x="1" y="4.5" width="10" height="5"/><rect x="3" y="9" width="6" height="2.5"/></svg>
          877-555-0193
        </li>
        <li>
          <svg viewBox="0 0 12 12" aria-hidden="true"><path d="M0.5 2.5h11v7h-11z M0.5 2.5 6 6.5l5.5-4" stroke="#fff" stroke-width="0.8"/></svg>
          info@brantovelaw.com
        </li>
        <li>
          <svg viewBox="0 0 12 12" aria-hidden="true"><circle cx="6" cy="6" r="5.5"/><path d="M0.5 6h11M6 .5c-2 2.8-2 8.2 0 11M6 .5c2 2.8 2 8.2 0 11" stroke="#fff" stroke-width="0.7" fill="none"/></svg>
          www.brantovelaw.com
        </li>
      </ul>
    </div>
  </section>

</body>
</html>
```